TKA Electricial Contracting Services

Hi guys, after a design for my small electrical company, have logo design files to be incorporated into the layout, the basic concept is electrical contracting services for residential, commercial, industrial & data services, image is clean clear and strong,

Card format is to have a nice clean logo on front,with maybe the Residential – commercial – industrial - data, followed with licensed & insured, followed by contact details on backside of the card.

Target Market(s)

Residential, commercial, industrial sectors.

Industry/Entity Type

Electrical

Contact Information for Business Card

TKA logo,
Residential – commercial – industrial - data
REC: 61372
Email: tka@poralink.net.au
Phone: 0458 203 719

Requirements
Must have
• Clean & strong design.
Nice to have
• If possible, I would like the logo colours inverted so the text is orange and the background is black on the front of the card, then the backside of the card be the reverse colour
Should not have
• No Sparks, lightning bolts,

```html
<!DOCTYPE html>
<html lang="en">
<head>
<meta charset="utf-8">
<title>TKA Electricial Contracting Services – Business Card</title>
<link rel="stylesheet" href="https://fonts.googleapis.com/css2?family=Ubuntu:wght@400;500;700&display=swap">
<style>
  :root {
    --page-bg: #d9d9d9;
    --card-black: #0b0b0b;
    --card-black-soft: #1c1c1c;
    --orange: #f39a2c;
    --orange-light: #f7b23e;
    --orange-deep: #e8761f;
    --ink: #111111;
  }
  * { box-sizing: border-box; margin: 0; padding: 0; }
  html, body {
    width: 1200px; height: 1023px; overflow: hidden;
    background: var(--page-bg);
    font-family: "Ubuntu", sans-serif;
  }
  .sheet {
    width: 1200px; height: 1023px;
    display: flex; flex-direction: column; align-items: center;
    justify-content: center; gap: 28px;
  }
  .card {
    position: relative; width: 820px; height: 469px; overflow: hidden;
    box-shadow: 0 10px 24px rgba(0,0,0,.28);
  }
  .card--front {
    background: linear-gradient(135deg, var(--card-black-soft) 0%, var(--card-black) 60%);
    color: var(--orange);
  }
  .card--back {
    background: linear-gradient(135deg, var(--orange-deep) 0%, var(--orange) 50%, var(--orange-light) 100%);
    color: var(--ink);
  }
  .pattern-area {
    position: absolute; top: 0; right: 0; width: 360px; height: 200px;
  }
  .card--front .pattern-area {
    background: linear-gradient(200deg, rgba(243,154,44,.85) 0%, rgba(243,154,44,.35) 55%, rgba(243,154,44,0) 100%);
  }
  .card--back .pattern-area {
    background: linear-gradient(200deg, rgba(17,17,17,.8) 0%, rgba(17,17,17,.3) 55%, rgba(17,17,17,0) 100%);
  }
  .brand {
    position: absolute; left: 150px; top: 150px;
  }
  .brand__mark {
    font-size: 150px; font-weight: 700; line-height: .9; letter-spacing: -2px;
    color: var(--orange);
  }
  .brand__name {
    font-size: 34px; font-weight: 700; color: var(--orange);
    margin-top: 8px; margin-left: 40px;
  }
  .front-tagline {
    position: absolute; left: 40px; right: 40px; bottom: 34px;
    font-size: 23px; font-weight: 500; color: var(--orange);
    white-space: nowrap; text-align: center;
  }
  .contact {
    position: absolute; left: 70px; font-size: 30px; font-weight: 500;
    display: flex; align-items: center; gap: 14px;
  }
  .contact--phone { top: 150px; left: 380px; font-size: 34px; }
  .contact--email { top: 250px; }
  .contact__tag {
    display: inline-flex; align-items: center; justify-content: center;
    width: 26px; height: 26px; background: var(--ink); color: var(--orange-light);
    font-size: 17px; font-weight: 700;
  }
  .services {
    position: absolute; left: 70px; right: 40px; top: 320px;
    font-size: 25px; font-weight: 700; line-height: 1.3; text-align: center;
  }
</style>
</head>
<body>
<main class="sheet">
  <section class="card card--front" aria-label="Card front">
    <div class="pattern-area" role="img" aria-label="Decorative pattern of scattered orange squares"></div>
    <div class="brand">
      <div class="brand__mark">TKA</div>
      <div class="brand__name">Tyler Kane Electrical</div>
    </div>
    <p class="front-tagline">licenced &amp; insured Residential - commercial - industrial - data REC: 61372</p>
  </section>

  <section class="card card--back" aria-label="Card back">
    <div class="pattern-area" role="img" aria-label="Decorative pattern of scattered black squares"></div>
    <p class="contact contact--phone"><span class="contact__tag">P</span>0458 203 719</p>
    <p class="contact contact--email"><span class="contact__tag">E</span>tka@poralink.net.au</p>
    <div class="services">
      <p>New installations Additions Rewiring Repairs</p>
      <p>Maintenance 24 hours</p>
      <p>Faults and Emergency Assistance</p>
    </div>
  </section>
</main>
</body>
</html>
```